Plant Grower/Nursery needs a fun, professional and fresh 1/2 page print ad for a high profile gar...

We need a print ad for a garden tour geared towards plant enthusiasts that support California Native, natural and sustainable plants. A good percentage of our target market want a conservation and earth friendly approach to gardens/landscaping. We want to target this market, as well as, people who are looking for a pretty/colorful landscape that require little water/maintenance. **PLEASE LET US KNOW IF YOU HAVE QUESTIONS OR NEED MORE INFORMATION. WE ALSO HAVE MANY MORE PICTURES IF THESE DON'T WORK FOR YOUR DESIGN. ***THE AD CAN HAVE AS FEW AS 1 PHOTO - WE ARE POSTING SEVERAL IN HOPES THAT YOU CAN FIND WHAT IS PERFECT FOR YOUR IDEA!!Thank you

Target Market(s)

Gardeners, Landscapers, Landscape Designers/Architects, Cities and Municipalities.

Industry/Entity Type

Agriculture

Font styles to use
Serif
Sans Serif

Colors

Designer to choose colors to be used in the design.

Requirements
Must have
• We believe in growing regionally appropriate plants for Southern California that beatify our natural and urban landscapes.
• For over 20 years, our owners and staff take pride in providing timely, expert, and honest service.
Nice to have
• At least 1 photo. Eye catchy with a modern earthy feel.
• Hundreds of species/hybrids in stock of California Natives, Succulents, Ornamental Grasses, Standard Stock Items and Unique Plants.

```html
<!DOCTYPE html>
<html lang="en">
<head>
<meta charset="utf-8">
<title>Coastal Sage Growers – Print Ad</title>
<link rel="stylesheet" href="https://fonts.googleapis.com/css2?family=Fira+Sans+Condensed:wght@400;500;600&display=swap">
<style>
  :root {
    --page-bg: #e4e4e4;
    --paper: #ffffff;
    --leaf-dark: #0b7a3c;
    --leaf-mid: #00a651;
    --leaf-light: #3db54a;
    --ink-green: #1b7a3a;
    --photo-pale: #cfe0b4;
    --photo-green: #a3c685;
    --photo-deep: #6f9a5a;
    --photo-rose: #b5416a;
    --photo-shadow: #24301f;
  }
  * { margin: 0; padding: 0; box-sizing: border-box; }
  html, body {
    width: 1200px; height: 906px; overflow: hidden;
    background: var(--page-bg);
  }
  .ad {
    position: absolute; left: 0; top: 30px;
    width: 1200px; height: 846px;
    background: var(--paper);
    overflow: hidden;
    font-family: "Fira Sans Condensed", "Arial Narrow", sans-serif;
  }
  .ad-art { position: absolute; inset: 0; }
  .mission {
    position: absolute; left: 748px; top: 180px; width: 360px;
    text-align: center; color: #fff;
    font-weight: 500; font-size: 24.5px; line-height: 32.5px;
    letter-spacing: -0.3px;
  }
  .mission p + p { margin-top: 32.5px; }
  .brand {
    position: absolute; left: 51px; top: 718px;
    display: flex; align-items: center; gap: 10px;
  }
  .brand-dot {
    width: 72px; height: 72px; border-radius: 50%;
    background: var(--leaf-dark);
  }
  .brand-name {
    color: var(--ink-green); font-weight: 500;
    font-size: 18px; line-height: 22px; text-transform: uppercase;
    letter-spacing: 1px; margin-top: 10px;
  }
  .divider {
    position: absolute; left: 345px; top: 719px;
    width: 2px; height: 83px; background: var(--ink-green);
  }
  .stock {
    position: absolute; left: 381px; top: 741px;
    color: var(--ink-green); font-weight: 400;
    font-size: 15.5px; line-height: 24px; letter-spacing: -0.2px;
  }
</style>
</head>
<body>
<main class="ad">
  <svg class="ad-art" width="1200" height="846" viewBox="0 0 1200 846">
    <defs>
      <linearGradient id="photoBase" x1="0" y1="0" x2="1" y2="1">
        <stop offset="0" stop-color="var(--photo-green)"/>
        <stop offset="0.5" stop-color="var(--photo-pale)"/>
        <stop offset="1" stop-color="var(--photo-green)"/>
      </linearGradient>
      <radialGradient id="roseGlow">
        <stop offset="0" stop-color="var(--photo-rose)" stop-opacity="0.85"/>
        <stop offset="1" stop-color="var(--photo-rose)" stop-opacity="0"/>
      </radialGradient>
      <radialGradient id="shadeGlow">
        <stop offset="0" stop-color="var(--photo-shadow)" stop-opacity="0.9"/>
        <stop offset="1" stop-color="var(--photo-shadow)" stop-opacity="0"/>
      </radialGradient>
      <radialGradient id="deepGlow">
        <stop offset="0" stop-color="var(--photo-deep)" stop-opacity="0.7"/>
        <stop offset="1" stop-color="var(--photo-deep)" stop-opacity="0"/>
      </radialGradient>
      <radialGradient id="paleGlow">
        <stop offset="0" stop-color="#e3edcf" stop-opacity="0.9"/>
        <stop offset="1" stop-color="#e3edcf" stop-opacity="0"/>
      </radialGradient>
      <radialGradient id="leafTone" cx="0.5" cy="0.3" r="0.8">
        <stop offset="0" stop-color="var(--leaf-mid)"/>
        <stop offset="1" stop-color="var(--leaf-dark)"/>
      </radialGradient>
    </defs>

    <g class="photo" role="img" aria-label="Close-up photo of a succulent rosette with pale green leaves and red-tipped points">
      <rect x="0" y="0" width="1200" height="720" fill="url(#photoBase)"/>
      <ellipse cx="640" cy="470" rx="260" ry="230" fill="url(#paleGlow)"/>
      <ellipse cx="260" cy="380" rx="230" ry="260" fill="url(#paleGlow)"/>
      <ellipse cx="880" cy="110" rx="200" ry="140" fill="url(#shadeGlow)"/>
      <ellipse cx="330" cy="20" rx="230" ry="90" fill="url(#deepGlow)"/>
      <ellipse cx="120" cy="640" rx="200" ry="120" fill="url(#deepGlow)"/>
      <ellipse cx="30" cy="380" rx="90" ry="260" fill="url(#roseGlow)"/>
      <ellipse cx="330" cy="110" rx="160" ry="70" fill="url(#roseGlow)"/>
      <ellipse cx="560" cy="50" rx="160" ry="80" fill="url(#roseGlow)"/>
      <ellipse cx="1110" cy="90" rx="140" ry="140" fill="url(#roseGlow)"/>
      <ellipse cx="620" cy="520" rx="70" ry="70" fill="url(#roseGlow)"/>
      <ellipse cx="320" cy="560" rx="70" ry="90" fill="url(#roseGlow)"/>
      <ellipse cx="1140" cy="520" rx="120" ry="60" fill="url(#roseGlow)"/>
    </g>

    <path class="wave-band" fill="var(--leaf-light)"
          d="M0,629 C300,610 600,680 866,692 Q1050,698 1200,664 L1200,846 L0,846 Z"/>
    <path class="wave-paper" fill="var(--paper)"
          d="M0,679 C300,660 600,705 866,717 Q1050,720 1200,689 L1200,846 L0,846 Z"/>

    <path class="leaf-rim" fill="var(--leaf-light)"
          d="M1140,134 L1154,158 Q1140,230 1142,330 Q1144,500 1090,538 Q1060,557 990,559 L715,552 L701,532 L990,532 Q1050,530 1080,505 Q1122,470 1120,300 Q1118,190 1140,134 Z"/>
    <path class="leaf" fill="url(#leafTone)"
          d="M732,200 Q740,142 800,138 L1140,134 Q1118,190 1120,300 Q1122,470 1080,505 Q1050,530 990,532 L701,532 Q730,480 728,360 Q726,260 732,200 Z"/>
  </svg>

  <div class="mission">
    <p>We believe<br>in growing regionally<br>appropriate plants for Southern<br>California that beatify our<br>natural and urban landscapes.</p>
    <p>For over 20 years, our owners<br>and staff take pride in providing<br>timely, expert, and honest<br>service.</p>
  </div>

  <div class="brand">
    <span class="brand-dot"></span>
    <span class="brand-name">Coastal Sage<br>Growers</span>
  </div>
  <span class="divider"></span>
  <p class="stock">Hundreds of species/hybrids in stock of California Natives,<br>Succulents, Ornamental Grasses, Standard Stock Items and Unique Plants.</p>
</main>
</body>
</html>
```